We have developed a fully functional App called Corvalink. However, it requires a nicer GUI. You can see screenshots of our App on www.corvalink-example.com under "Tutorial". For those of you with Android, you can also install it. When you go to Corvalink-example.com, your phone will automatically redirect you to download. From there, you'll get a better idea of what our App looks like and how your design can make it way better. Please note we expect a design idea for most screens (there's about 8 screens) but do just one screen first and if you win, you can do the other 8 after.

Target Market(s)

People looking for dating / flirting

Industry/Entity Type

Android

Requirements
Must have
• sleek looking

```html
<!DOCTYPE html>
<html lang="en">
<head>
<meta charset="utf-8">
<title>Corvalink – Members</title>
<link rel="stylesheet" href="https://fonts.googleapis.com/css2?family=Roboto:wght@400;500;700&display=swap">
<style>
  :root {
    --page-bg: #ececec;
    --header-purple: #6a0a4c;
    --card-teal: #007d90;
    --card-plum: #6c0049;
    --list-bg: #ffffff;
    --button-blue: #3cb2dc;
    --nav-blue: #4fc0ea;
    --nav-active: #38a9d9;
    --nav-divider: #74cfee;
    --text-white: #ffffff;
    --chevron: #c9d6dc;
    --avatar-ring: #c8c8c8;
    --status-online: #1fc21f;
    --status-away: #e0a30c;
    --status-offline: #a6a6a6;
  }
  * { box-sizing: border-box; margin: 0; padding: 0; }
  html, body {
    width: 713px; height: 1200px; overflow: hidden;
    background: var(--page-bg);
    font-family: "Roboto", Arial, sans-serif;
    color: var(--text-white);
  }
  .app-screen {
    position: absolute; left: 103px; top: 218px;
    width: 500px; height: 752px;
    background: var(--list-bg);
    overflow: hidden;
  }
  .top-bar {
    position: absolute; left: 0; top: 0; width: 500px; height: 72px;
    background: var(--header-purple);
  }
  .bar-button {
    position: absolute; top: 18px; width: 56px; height: 37px;
    background: var(--button-blue); border-radius: 3px;
    display: flex; align-items: center; justify-content: center;
    box-shadow: 0 2px 0 rgba(0,0,0,.25);
  }
  .bar-button.back { left: 14px; }
  .bar-button.refresh { right: 16px; }
  .brand {
    position: absolute; left: 50%; top: 36px; transform: translate(-50%, -50%);
    display: flex; align-items: center; gap: 10px;
  }
  .brand-dot { width: 18px; height: 18px; border-radius: 50%; background: var(--button-blue); }
  .brand-name { font-size: 30px; font-weight: 500; color: var(--chevron); letter-spacing: .5px; }

  .member-list {
    position: absolute; left: 6px; top: 79px; width: 487px; height: 586px;
    overflow: hidden;
  }
  .member-card {
    position: absolute; left: 0; width: 487px; height: 125px;
    border-radius: 3px;
  }
  .member-card.teal { background: var(--card-teal); }
  .member-card.plum { background: var(--card-plum); }
  .avatar {
    position: absolute; left: 10px; top: 7px; width: 111px; height: 111px;
    border-radius: 50%; border: 4px solid var(--avatar-ring);
  }
  .member-name { position: absolute; left: 143px; top: 12px; font-size: 16px; font-weight: 700; }
  .member-tagline { position: absolute; left: 143px; top: 37px; font-size: 12px; }
  .member-city { position: absolute; left: 146px; top: 88px; font-size: 14px; font-weight: 700; }
  .member-country { position: absolute; left: 147px; top: 105px; font-size: 11px; font-weight: 500; }
  .member-status {
    position: absolute; right: 26px; top: 100px; font-size: 14px;
    display: flex; align-items: center; gap: 8px;
  }
  .status-dot { width: 17px; height: 17px; border-radius: 50%; }
  .status-dot.online { background: var(--status-online); }
  .status-dot.away { background: var(--status-away); }
  .status-dot.offline { background: var(--status-offline); }
  .mail-flag { margin-right: 12px; }
  .chevron { position: absolute; right: 8px; top: 36px; }

  .tab-bar {
    position: absolute; left: 0; top: 665px; width: 500px; height: 85px;
    display: flex; background: var(--nav-blue);
  }
  .tab {
    flex: 1 1 0; display: flex; flex-direction: column; align-items: center;
    justify-content: flex-end; padding-bottom: 14px; gap: 9px;
    font-size: 16px; font-weight: 500;
  }
  .tab + .tab { border-left: 1px solid var(--nav-divider); }
  .tab.active { background: var(--nav-active); flex-basis: 0; flex-grow: 1.05; }
</style>
</head>
<body>
<main class="app-screen">
  <header class="top-bar">
    <div class="bar-button back" aria-label="Back">
      <svg width="16" height="24" viewBox="0 0 16 24"><path d="M12 3 L4 12 L12 21" fill="none" stroke="#fff" stroke-width="4" stroke-linecap="round" stroke-linejoin="round"/></svg>
    </div>
    <div class="brand"><span class="brand-dot"></span><span class="brand-name">Corvalink</span></div>
    <div class="bar-button refresh" aria-label="Refresh">
      <svg width="28" height="26" viewBox="0 0 28 26" fill="none" stroke="#fff" stroke-width="3.2">
        <path d="M4 11 A10 10 0 0 1 22 7"/><path d="M24 15 A10 10 0 0 1 6 19"/>
        <path d="M18 7 H23 V2" stroke-linejoin="miter"/><path d="M10 19 H5 V24" stroke-linejoin="miter"/>
      </svg>
    </div>
  </header>

  <section class="member-list">
    <article class="member-card teal" style="top:0">
      <div class="avatar" role="img" aria-label="Profile photo" style="background:radial-gradient(circle at 45% 40%,#6d5a55,#2b2325 70%)"></div>
      <h2 class="member-name">Sweetguy, 29</h2>
      <p class="member-tagline">“! Sweet, Never sour”</p>
      <p class="member-city">New York</p>
      <p class="member-country">U.S.A</p>
      <div class="member-status"><span class="status-dot online"></span>Online</div>
      <svg class="chevron" width="18" height="28" viewBox="0 0 18 28"><path d="M3 3 L14 14 L3 25" fill="none" stroke="var(--chevron)" stroke-width="3"/></svg>
    </article>

    <article class="member-card plum" style="top:128px">
      <div class="avatar" role="img" aria-label="Profile photo" style="background:radial-gradient(circle at 50% 45%,#7a4a58,#231c2c 72%)"></div>
      <h2 class="member-name">Sensual Mirela, 25</h2>
      <p class="member-tagline">!!!Goodess and Temptress lives here</p>
      <p class="member-city">New York</p>
      <p class="member-country">U.S.A</p>
      <div class="member-status"><span class="status-dot online"></span>Online</div>
      <svg class="chevron" width="18" height="28" viewBox="0 0 18 28"><path d="M3 3 L14 14 L3 25" fill="none" stroke="var(--chevron)" stroke-width="3"/></svg>
    </article>

    <article class="member-card teal" style="top:257px">
      <div class="avatar" role="img" aria-label="Profile photo" style="background:radial-gradient(circle at 50% 45%,#e6c79c,#a8865c 75%)"></div>
      <h2 class="member-name">Sweetguy, 29</h2>
      <p class="member-tagline">“! Sweet, Never sour”</p>
      <p class="member-city">New York</p>
      <p class="member-country">U.S.A</p>
      <div class="member-status">
        <svg class="mail-flag" width="20" height="14" viewBox="0 0 20 14"><rect x="0.5" y="0.5" width="19" height="13" fill="#c9d0d4" stroke="#8a9499"/><path d="M1 1 L10 8 L19 1" fill="none" stroke="#8a9499"/></svg>
        <span class="status-dot away"></span>Away
      </div>
      <svg class="chevron" width="18" height="28" viewBox="0 0 18 28"><path d="M3 3 L14 14 L3 25" fill="none" stroke="var(--chevron)" stroke-width="3"/></svg>
    </article>

    <article class="member-card plum" style="top:387px">
      <div class="avatar" role="img" aria-label="Profile photo" style="background:radial-gradient(circle at 50% 45%,#9a7660,#4a3a34 75%)"></div>
      <h2 class="member-name">Marco Velendi, 30</h2>
      <p class="member-tagline">“! Sweet, Never sour”</p>
      <p class="member-city">New York</p>
      <p class="member-country">U.S.A</p>
      <div class="member-status"><span class="status-dot offline"></span>Offline</div>
      <svg class="chevron" width="18" height="28" viewBox="0 0 18 28"><path d="M3 3 L14 14 L3 25" fill="none" stroke="var(--chevron)" stroke-width="3"/></svg>
    </article>

    <article class="member-card teal" style="top:517px">
      <div class="avatar" role="img" aria-label="Profile photo" style="background:radial-gradient(circle at 50% 45%,#7a4a58,#231c2c 72%)"></div>
      <h2 class="member-name">Sweetguy, 29</h2>
      <p class="member-tagline">“! Sweet, Never sour”</p>
      <svg class="chevron" width="18" height="28" viewBox="0 0 18 28"><path d="M3 3 L14 14 L3 25" fill="none" stroke="var(--chevron)" stroke-width="3"/></svg>
    </article>
  </section>

  <nav class="tab-bar">
    <div class="tab">
      <svg width="36" height="18" viewBox="0 0 36 18" fill="#fff"><rect y="0" width="36" height="3"/><rect y="7" width="36" height="3"/><rect y="14" width="36" height="3"/></svg>
      Main
    </div>
    <div class="tab active">
      <svg width="26" height="18" viewBox="0 0 26 18" fill="none" stroke="#fff" stroke-width="2"><rect x="1" y="1" width="24" height="16"/><path d="M1 1 L13 10 L25 1"/></svg>
      Message
    </div>
    <div class="tab">
      <svg width="26" height="26" viewBox="0 0 26 26" fill="none" stroke="#fff" stroke-width="2">
        <circle cx="13" cy="13" r="4"/>
        <path d="M11 2 H15 L15.8 5.3 L18.6 6.9 L21.8 5.8 L23.8 9.3 L21.3 11.6 V14.4 L23.8 16.7 L21.8 20.2 L18.6 19.1 L15.8 20.7 L15 24 H11 L10.2 20.7 L7.4 19.1 L4.2 20.2 L2.2 16.7 L4.7 14.4 V11.6 L2.2 9.3 L4.2 5.8 L7.4 6.9 L10.2 5.3 Z"/>
      </svg>
      Settings
    </div>
  </nav>
</main>
</body>
</html>
```